Casa Orvella Postcard

Please refer to our site for inspiration - I know this is alot of info but ?

Casa Orvella Reception Hall
4182C Tamsen Ave, Benicia, CA 707-555-0148
www.Casa-Orvella.example

Located in Benicia, California, we are a new venue that can host a variety of events. We can provide an exceptional space for your next party, reception, quinceañera, birthday party, or meeting! We treat each client with respect and go out of our way to accommodate all of your needs and make your event a success. Conveniently located just off the 680/780 junction, Casa Orvella is located in a safe, well-lit area with a large private parking area.

The space comes prepared with everything you need to get your party started – chairs and tables with tablecloths, a well-equipped kitchen, and incredible decorations to set the perfect backdrop to your event! Rent just the Lounge for a more intimate get-together, or add the Main Hall for your large sit-down event.

Lounge – Beautiful 1,600 ft2 entry room featuring large living room with conversation sofa seating for 40+ Sound system  Pass-through bar with seating  Fully-equipped 200 ft2 kitchen with
4-burner gas stove, oven, large double sink, full-size refrigerator, 2 microwaves, and ice machine, plus lots of storage and counter space  Newly-remodeled Men’s and Women’s bathrooms

Main Hall – Spacious 24’x80’ room with seating for up to 160 people  2,000 ft2  72” round tables with chairs, each seating up to 8 guests  DJ stand and Sound system  Atmospheric lighting
_______________________________________
Pricing -
Daytime Parties
Available 8AM-2PM
4-hour minimum

Lounge and Kitchen Only
Fri - Sat - Sun : $80/hr
Mon - Thurs : $60/hr

All Areas: Lounge, Kitchen, Main Hall, and Backyard
Fri - Sat - Sun : $120/hr
Mon - Thurs : $100/hr
___________________________________________
Evening Events
Available 3PM-12AM
5-hour minimum

Lounge and Kitchen Only -
Fri - Sat - Sun : $100/hr
Mon - Thurs : $50/hr

Fri - Sat - Sun : $160/hr
Mon - Thurs : $75/hr
___________________________________________________
Looking for a different time frame, all-day rental, or other special request? Let us know!
We'd be happy to provide you with a custom quote for your event.
Updates

I am not going to mail this postcard - only a hand out I need info and pricing on back

Target Market(s)

This is a hand out - will not be mailed

Only need my text on back

Industry/Entity Type

Parking

Requirements
Must have
• Text and pricing on back
Should not have
• Vintage feel to it

```html
<!DOCTYPE html>
<html lang="en">
<head>
<meta charset="utf-8">
<title>Casa Orvella Postcard</title>
<link href="https://fonts.googleapis.com/css2?family=Tinos:ital,wght@0,400;0,700;1,400&family=Hind:wght@400;500;600&display=swap" rel="stylesheet">
<style>
:root{
  --paper:#ffffff;
  --ink:#1c1c1c;
  --cream:#f4efe6;
  --gold:#d9b068;
  --ceiling:#3e2f25;
  --wall:#d9c6a4;
  --wall-warm:#b99a72;
  --sofa:#5a4232;
  --floor:#2a1f18;
  --rule:#222;
}
*{margin:0;padding:0;box-sizing:border-box}
html,body{width:1200px;height:1200px;overflow:hidden;background:var(--paper)}
body{position:relative;font-family:'Hind',Arial,sans-serif;color:var(--ink)}
.abs{position:absolute}
.serif{font-family:'Tinos','Times New Roman',serif}

/* front */
.card-shadow{box-shadow:2px 3px 6px rgba(0,0,0,.35);background:var(--paper)}
.front-sheet{left:167px;top:19px;width:867px;height:560px}
.back-sheet{left:167px;top:618px;width:867px;height:560px}
.front-photo{left:180px;top:33px;width:840px;height:532px;
  background:
    radial-gradient(ellipse 60% 40% at 55% 42%,rgba(235,222,196,.55),rgba(235,222,196,0) 70%),
    linear-gradient(180deg,var(--ceiling) 0%,#7a6350 12%,var(--wall-warm) 24%,var(--wall) 38%,#b8a283 50%,var(--sofa) 62%,#46342a 78%,var(--floor) 100%);}
.front-shade{left:180px;top:460px;width:840px;height:105px;background:linear-gradient(rgba(25,18,12,0),rgba(25,18,12,.75))}
.kicker{left:205px;top:42px;font-size:17px;color:var(--cream);letter-spacing:.5px}
.headline{left:205px;top:68px;font-size:33px;line-height:38px;color:var(--cream)}
.headline .accent{color:var(--gold);display:block}
.site{right:196px;top:42px;font-size:12.5px;color:var(--cream);letter-spacing:.5px}
.brand-front{left:210px;top:482px;font-size:30px;color:var(--cream)}
.tagline-front{left:211px;top:519px;font-size:12.5px;font-style:italic;color:var(--cream);letter-spacing:.3px}
.front-divider{left:400px;top:478px;width:1px;height:64px;background:var(--cream)}
.front-info{left:421px;top:483px;color:var(--cream)}
.front-info .hall{font-size:15px;letter-spacing:.3px}
.contact-line{display:flex;align-items:center;font-size:14px;margin-top:3px;white-space:nowrap}
.contact-line .sep{margin:0 15px}
.contact-line svg{margin-right:9px}
.front-info .blurb{font-size:12.5px;letter-spacing:1.75px;margin-top:4px;white-space:nowrap}

/* back */
.thumb{left:180px;width:182px;height:128px}
.t1{top:632px;background:linear-gradient(180deg,#3d3029 0%,#cfc4b0 35%,#8e7b66 60%,#4a3a2e 100%)}
.t2{top:767px;background:radial-gradient(circle at 50% 35%,#d4aa7c,#8a6a4e 45%,#3e3028 85%)}
.t3{top:902px;background:linear-gradient(180deg,#3b2e26 0%,#cbbfad 30%,#a89986 55%,#e2dbd0 70%,#6c5d4e 100%)}
.t4{top:1037px;background:linear-gradient(180deg,#3a2c24 0%,#6e5a4a 35%,#d7d0c6 60%,#3a2b22 100%)}
.brand-back{left:378px;top:643px;font-size:32px}
.tagline-back{left:380px;top:680px;font-size:12.5px;font-style:italic}
.copy{left:378px;top:707px;width:636px;font-size:10.1px;line-height:11.7px;letter-spacing:.1px}
.copy h3{font-size:10.1px;font-weight:600;text-decoration:underline;margin-top:11.7px}
.copy p{margin:0}
.pricing{left:421px;top:930px;width:560px}
.pricing h2{width:530px;font-size:14px;font-weight:400;letter-spacing:.3px;border-bottom:1px solid var(--rule);line-height:16px}
.price-cols{display:flex;margin-top:8px}
.price-col{flex:0 0 279px;font-size:10.1px;line-height:11.7px;letter-spacing:.1px}
.price-col h4{font-size:10.1px;font-weight:600;text-decoration:underline}
.price-col .block{margin-bottom:11.7px}
.footer{left:380px;top:1111px}
.footer .hall{font-size:16px;color:var(--ink)}
.footer .contact-line{font-size:14px;margin-top:2px}
</style>
</head>
<body>

<div class="abs card-shadow front-sheet"></div>
<div class="abs card-shadow back-sheet"></div>

<section class="card-front">
  <div class="abs front-photo" role="img" aria-label="Photo of the lounge with brown sofas, pendant globe lights and tall windows"></div>
  <div class="abs front-shade"></div>
  <div class="abs kicker serif">WHEN</div>
  <div class="abs headline serif">YOU DESIRE<span class="accent">EXCEPTIONAL</span></div>
  <div class="abs site serif">www.casa-orvella.example</div>
  <div class="abs brand-front serif">Casa Orvella</div>
  <div class="abs tagline-front">receptions . parties . memories</div>
  <div class="abs front-divider"></div>
  <div class="abs front-info serif">
    <div class="hall">CASA ORVELLA RECEPTION HALL</div>
    <div class="contact-line">4182C Tamsen Ave, Benicia, CA<span class="sep">|</span>
      <svg width="11" height="11" viewBox="0 0 24 24"><path fill="currentColor" d="M6.6 10.8a15 15 0 0 0 6.6 6.6l2.2-2.2c.3-.3.7-.4 1-.2 1.1.4 2.3.6 3.6.6.6 0 1 .4 1 1V20c0 .6-.4 1-1 1A17 17 0 0 1 3 4c0-.6.4-1 1-1h3.5c.6 0 1 .4 1 1 0 1.3.2 2.5.6 3.6.1.3 0 .7-.2 1z"/></svg>707-555-0148<span class="sep">|</span>
      <svg width="12" height="9" viewBox="0 0 24 18"><rect width="24" height="18" fill="currentColor"/><path d="M1 1l11 9 11-9" fill="none" stroke="#3a2c22" stroke-width="2"/></svg>events@casa-orvella.example</div>
    <div class="blurb">An exceptional space for party, reception, quinceañera, birthday party, or meeting!</div>
  </div>
</section>

<section class="card-back">
  <div class="abs thumb t1" role="img" aria-label="Photo of the entry lounge seating area"></div>
  <div class="abs thumb t2" role="img" aria-label="Photo of two armchairs beside a lamp and floral wall art"></div>
  <div class="abs thumb t3" role="img" aria-label="Photo of a buffet table set with food in the hall"></div>
  <div class="abs thumb t4" role="img" aria-label="Photo of the main hall with round tables and string lights"></div>

  <div class="abs brand-back serif">Casa Orvella</div>
  <div class="abs tagline-back">receptions . parties . memories</div>

  <div class="abs copy">
    <p>Located in Benicia, California, we are a new venue that can host a variety of events. We can provide an exceptional space for your next party, reception, quinceañera, birthday party, or meeting! We treat each client with respect and go out of our way to accommodate all of your needs and make your event a success.</p>
    <h3>Three Areas to Fit Any Size Party!</h3>
    <h3>Entry Lounge</h3>
    <p>Beautiful 1,600 sq ft entry room featuring large living room with conversation sofa seating for 40 – Sound system – Pass-through bar with seating – &nbsp;Newly-remodeled Men’s and Women’s bathrooms.</p>
    <h3>Kitchen</h3>
    <p>Fully-equipped 200 sq ft kitchen – 4-burner gas stove and oven – Large double sink – Full-size refrigerator – 2 microwaves – Ice machine – Lots of storage and counter space</p>
    <h3>Main Hall</h3>
    <p>Spacious 24’x80’ room with seating for up to 160 people – 2,000 sq ft – 72” round tables with chairs, each seating up to 8 guests – DJ stand and Sound system – Atmospheric lighting.</p>
  </div>

  <div class="abs pricing">
    <h2>PRICING</h2>
    <div class="price-cols">
      <div class="price-col">
        <div class="block"><h4>Daytime Parties</h4>Available 8AM-2PM<br>4-hour minimum</div>
        <div class="block"><h4>Lounge and Kitchen Only</h4>Fri - Sat - Sun : $80/hr<br>Mon - Thurs : $60/hr</div>
        <div class="block"><h4>All Areas: Lounge, Kitchen, Main Hall, and Backyard</h4>Fri - Sat - Sun : $120/hr<br>Mon - Thurs : $100/hr</div>
      </div>
      <div class="price-col">
        <div class="block"><h4>Evening Events</h4>Available 3PM-12AM<br>5-hour minimum</div>
        <div class="block"><h4>Lounge and Kitchen Only</h4>Fri - Sat - Sun : $100/hr<br>Mon - Thurs : $50/hr</div>
        <div class="block"><h4>All Areas: Lounge, Kitchen, Main Hall, and Backyard</h4>Fri - Sat - Sun : $160/hr<br>Mon - Thurs : $75/hr</div>
      </div>
    </div>
  </div>

  <div class="abs footer serif">
    <div class="hall">CASA ORVELLA RECEPTION HALL</div>
    <div class="contact-line">4182C Tamsen Ave, Benicia, CA<span class="sep">|</span>
      <svg width="11" height="11" viewBox="0 0 24 24"><path fill="currentColor" d="M6.6 10.8a15 15 0 0 0 6.6 6.6l2.2-2.2c.3-.3.7-.4 1-.2 1.1.4 2.3.6 3.6.6.6 0 1 .4 1 1V20c0 .6-.4 1-1 1A17 17 0 0 1 3 4c0-.6.4-1 1-1h3.5c.6 0 1 .4 1 1 0 1.3.2 2.5.6 3.6.1.3 0 .7-.2 1z"/></svg>707-555-0148<span class="sep">|</span>
      <svg width="12" height="9" viewBox="0 0 24 18"><rect width="24" height="18" fill="currentColor"/><path d="M1 1l11 9 11-9" fill="none" stroke="#fff" stroke-width="2"/></svg>events@casa-orvella.example</div>
  </div>
</section>

</body>
</html>
```